Digital Signage Mockup template

I would like to have some mock ups for digital signage templates(content on screens) - deliverable should be psd file + png export; it is to promote a digital signage business and can be fictive examples about fictive company as well as of a real example; use recent design trends (material design or more recent)
- corporate - welcome board (weather, news, anniversary wishes, visiting guests, ticker text) : 3 variations + landscape and portrait
- corporate : meeting room reservation screen - landscape only ; 2 variations
see example as inspiration :
https://www.lumaquist.com/sites/default/files/reception%20landscape.png
https://www.brivotane.com/blog/corporate-digital-signage/
- Nero Sans

```html
<!DOCTYPE html>
<html lang="en">
<head>
<meta charset="utf-8">
<title>Digital Signage Templates</title>
<link rel="stylesheet" href="https://fonts.googleapis.com/css2?family=Montserrat:wght@200;300;400;500;600;700;900&display=swap">
<style>
:root{
  --canvas:#c6c6c6;
  --blue:#4272d0;
  --blue-deep:#2c5bc4;
  --navy:#0d2763;
  --magenta:#c4168f;
  --plum:#86104f;
  --charcoal:#20242e;
  --ink:#1b1f27;
  --orange:#f28a00;
  --white:#ffffff;
}
*{margin:0;padding:0;box-sizing:border-box}
html,body{width:1200px;height:1200px;overflow:hidden;background:var(--canvas)}
body{position:relative;font-family:'Montserrat',sans-serif;color:var(--white)}
.panel{position:absolute;overflow:hidden}
.abs{position:absolute}
.photo{position:absolute}
.welcome{font-weight:900;letter-spacing:-0.5px;line-height:1}
.lead{font-weight:400;opacity:.9}
.clock{font-weight:200;line-height:1;letter-spacing:.5px}
.date{font-weight:500}
.divider{position:absolute;width:.8px;background:rgba(255,255,255,.7)}
.wx svg{display:block}
.wx p{font-weight:500;line-height:1.2}
.feed .hd{font-weight:700;border-bottom:.6px solid rgba(255,255,255,.75);padding-bottom:2px;margin-bottom:3px}
.feed .copy{line-height:1.6;opacity:.9}
.brand{display:flex;align-items:center;gap:4px;font-weight:900;color:var(--ink)}
.brand i{display:block;background:var(--blue-deep)}
.brand.light{color:var(--white)}
.brand.light i{background:var(--white);border-radius:50%}
.brand.orange i{background:var(--orange)}
.btn{position:absolute;display:flex;align-items:center;justify-content:center;font-weight:700}
</style>
</head>
<body>

<svg width="0" height="0" style="position:absolute">
  <symbol id="icon-sun-cloud" viewBox="0 0 40 32">
    <g fill="none" stroke="#fff" stroke-width="1.4" stroke-linecap="round">
      <path d="M19 10a7 7 0 0 1 13 4"/>
      <line x1="26" y1="1" x2="26" y2="4"/><line x1="34" y1="5" x2="32" y2="7"/>
      <line x1="38" y1="13" x2="35" y2="13"/><line x1="18" y1="5" x2="20" y2="7"/>
      <path d="M9 29h22a6 6 0 0 0 0-12 9 9 0 0 0-17-2 7 7 0 0 0-5 14z"/>
    </g>
  </symbol>
</svg>

<!-- Landscape welcome, blue -->
<section class="panel" style="left:11px;top:13px;width:389px;height:218px;background:var(--white)">
  <div class="photo" role="img" aria-label="Blurred mountain valley landscape under a blue sky" style="left:0;top:0;width:216px;height:194px;background:linear-gradient(180deg,#3f6ed3 0%,#5b86d8 45%,#6b8fa0 70%,#6c6a4c 100%)"></div>
  <h1 class="abs welcome" style="left:22px;top:14px;font-size:36px">welcome</h1>
  <p class="abs lead" style="left:24px;top:53px;font-size:5.5px">Lorem ipsum dolor sit amet, consectetur adipiscing elit.</p>
  <p class="abs clock" style="left:24px;top:90px;font-size:30px">11:24</p>
  <p class="abs date" style="left:28px;top:125px;font-size:8.5px">August 5 , 2018</p>
  <span class="divider" style="left:112px;top:82px;height:62px"></span>
  <div class="abs wx" style="left:133px;top:86px"><svg width="36" height="29"><use href="#icon-sun-cloud"/></svg><p style="font-size:7px;margin-top:9px">Currently Partly<br>Sunny 78°F</p></div>
  <div class="abs brand" style="left:16px;top:201px;font-size:6.5px"><i style="width:7px;height:7px"></i>YOUR LOGO</div>
  <div class="abs feed" style="left:216px;top:0;width:173px;height:218px;background:var(--blue);padding:22px 12px 0 0">
    <div style="font-size:4.3px">
      <p class="hd" style="font-size:5.5px;padding-left:27px">News</p>
      <p class="copy" style="padding-left:28px">Lorem ipsum dolor sit amet, consectetur adipiscing elit. Sed ornare, metus non cursus volutpat, ligula odio faucibus turpis, non tincidunt nunc nunc quis elit.</p>
      <p class="hd" style="font-size:5.5px;padding-left:27px;margin-top:11px">Anniversary wishes</p>
      <p class="copy" style="padding-left:28px">Lorem ipsum dolor sit amet, consectetur adipiscing elit. Sed ornare, metus non cursus volutpat, ligula odio faucibus turpis, non tincidunt nunc nunc quis elit.</p>
      <p class="hd" style="font-size:5.5px;padding-left:27px;margin-top:11px">visiting guests</p>
      <p class="copy" style="padding-left:28px">Lorem ipsum dolor sit amet, consectetur adipiscing elit. Sed ornare, metus non cursus volutpat, ligula odio faucibus turpis, non tincidunt nunc nunc quis elit. Lorem ipsum dolor sit amet, consectetur adipiscing elit. Sed ornare, metus non cursus volutpat, ligula odio faucibus turpis, non tincidunt nunc nunc quis elit.</p>
    </div>
  </div>
</section>

<!-- Landscape welcome, magenta -->
<section class="panel" style="left:10px;top:242px;width:390px;height:219px">
  <div class="photo" role="img" aria-label="City skyline tinted magenta" style="inset:0;background:linear-gradient(180deg,var(--magenta) 0%,#b3157f 55%,var(--plum) 100%)"></div>
  <svg class="abs" style="left:0;top:0" width="390" height="219" viewBox="0 0 390 219">
    <path d="M0 0H232C190 50 120 84 0 88Z" fill="#fff"/>
    <path d="M390 172C372 198 358 210 340 219H390Z" fill="#fff"/>
  </svg>
  <p class="abs" style="left:22px;top:14px;font-size:16px;font-weight:300;color:var(--ink);line-height:1">Welcome to</p>
  <p class="abs" style="left:22px;top:30px;font-size:16px;font-weight:700;color:var(--ink);line-height:1">Lorem Ipsum</p>
  <p class="abs clock" style="left:252px;top:14px;font-size:22px">11:24</p>
  <p class="abs date" style="left:255px;top:40px;font-size:6px">August 5 , 2018</p>
  <span class="divider" style="left:314px;top:12px;height:38px"></span>
  <div class="abs wx" style="left:330px;top:14px"><svg width="24" height="19"><use href="#icon-sun-cloud"/></svg><p style="font-size:5px;margin-top:4px">Currently Partly<br>Sunny 78°F</p></div>
  <div class="abs feed" style="left:48px;top:94px;width:100px;font-size:4.5px"><p class="hd" style="font-size:6px;border:0">Visiting guests</p><p class="copy">Lorem ipsum dolor sit amet, consectetur adipiscing elit. Sed ornare, metus non cursus volutpat, ligula odio faucibus turpis, non tincidunt nunc nunc quis elit.</p></div>
  <div class="abs feed" style="left:156px;top:94px;width:100px;font-size:4.5px"><p class="hd" style="font-size:6px;border:0">Anniversary wishes</p><p class="copy">Lorem ipsum dolor sit amet, consectetur adipiscing elit. Sed ornare, metus non cursus volutpat, ligula odio faucibus turpis, non tincidunt nunc nunc quis elit.</p></div>
  <div class="abs feed" style="left:268px;top:94px;width:82px;font-size:4.5px"><p class="hd" style="font-size:6px;border:0">News</p><p class="copy">Lorem ipsum dolor sit amet, consectetur adipiscing elit. Sed ornare, metus non cursus volutpat, ligula odio faucibus turpis, non tincidunt nunc nunc quis elit.</p></div>
  <p class="abs" style="left:24px;top:197px;font-size:5px;font-weight:700">Lorem ipsum dolor sit amet, consectetur adipiscing elit.&nbsp; Consectetur adipiscing elit.</p>
  <div class="abs brand orange" style="left:347px;top:200px;font-size:5px;line-height:1"><i style="width:6px;height:6px"></i>LOREM<br>IPSUM</div>
</section>

<!-- Landscape welcome, dusk -->
<section class="panel" style="left:11px;top:470px;width:392px;height:219px">
  <div class="photo" role="img" aria-label="City at dusk with an orange horizon" style="inset:0;background:linear-gradient(180deg,#123273 0%,#28559d 35%,#6c79a0 55%,#e1854a 68%,#59455a 76%,#1b2238 100%)"></div>
  <h1 class="abs welcome" style="left:22px;top:16px;font-size:36px">welcome</h1>
  <p class="abs lead" style="left:24px;top:54px;font-size:5.5px">Lorem ipsum dolor sit amet, consectetur adipiscing elit.</p>
  <p class="abs clock" style="left:24px;top:90px;font-size:30px">11:24</p>
  <p class="abs date" style="left:28px;top:125px;font-size:8.5px">August 5 , 2018</p>
  <span class="divider" style="left:113px;top:82px;height:62px"></span>
  <div class="abs wx" style="left:134px;top:86px"><svg width="36" height="29"><use href="#icon-sun-cloud"/></svg><p style="font-size:7px;margin-top:9px">Currently Partly<br>Sunny 78°F</p></div>
  <div class="abs" style="left:0;top:181px;width:221px;height:20px;background:var(--blue-deep)"></div>
  <div class="abs brand light" style="left:25px;top:186px;font-size:10px"><i style="width:10px;height:10px"></i>LOGO</div>
  <div class="abs feed" style="left:221px;top:13px;width:155px;height:195px;background:rgba(13,39,99,.55);border:.8px solid rgba(255,255,255,.6);padding:10px 10px 0 0;font-size:4.2px">
    <p class="hd" style="font-size:5.5px;padding-left:13px">News</p>
    <p class="copy" style="padding-left:14px">Lorem ipsum dolor sit amet, consectetur adipiscing elit. Sed ornare, metus non cursus volutpat, ligula odio faucibus turpis, non tincidunt nunc nunc quis elit.</p>
    <p class="hd" style="font-size:5.5px;padding-left:13px;margin-top:10px">Anniversary wishes</p>
    <p class="copy" style="padding-left:14px">Lorem ipsum dolor sit amet, consectetur adipiscing elit. Sed ornare, metus non cursus volutpat, ligula odio faucibus turpis, non tincidunt nunc nunc quis elit.</p>
    <p class="hd" style="font-size:5.5px;padding-left:13px;margin-top:10px">visiting guests</p>
    <p class="copy" style="padding-left:14px">Lorem ipsum dolor sit amet, consectetur adipiscing elit. Sed ornare, metus non cursus volutpat, ligula odio faucibus turpis, non tincidunt nunc nunc quis elit. Lorem ipsum dolor sit amet, consectetur adipiscing elit. Sed ornare, metus non cursus volutpat, ligula odio faucibus turpis, non tincidunt nunc nunc quis elit.</p>
  </div>
</section>

<!-- Portrait welcome, blue -->
<section class="panel" style="left:408px;top:13px;width:255px;height:454px;background:var(--blue)">
  <div class="photo" role="img" aria-label="Blurred mountain landscape under a blue sky" style="left:0;top:0;width:255px;height:197px;background:linear-gradient(180deg,#3e6dd2 0%,#5a86d9 50%,#7b93a6 80%,#6f6c55 100%)"></div>
  <h1 class="abs welcome" style="left:0;width:255px;text-align:center;top:24px;font-size:40px">welcome</h1>
  <p class="abs lead" style="left:0;width:255px;text-align:center;top:73px;font-size:6.5px">Lorem ipsum dolor sit amet, consectetur adipiscing elit.</p>
  <p class="abs clock" style="left:30px;top:114px;font-size:36px">11:24</p>
  <p class="abs date" style="left:34px;top:155px;font-size:10px">August 5 , 2018</p>
  <span class="divider" style="left:134px;top:105px;height:75px"></span>
  <div class="abs wx" style="left:160px;top:110px"><svg width="42" height="34"><use href="#icon-sun-cloud"/></svg><p style="font-size:8.5px;margin-top:10px;margin-left:-2px">Currently Partly<br>Sunny 78°F</p></div>
  <div class="abs feed" style="left:25px;top:215px;width:205px;font-size:4.5px">
    <p class="hd" style="font-size:6px;padding-left:32px;margin-left:0">News</p>
    <p class="copy" style="padding-left:33px">Lorem ipsum dolor sit amet, consectetur adipiscing elit. Sed ornare, metus non cursus volutpat, ligula odio faucibus turpis, non tincidunt nunc nunc quis elit.</p>
    <p class="hd" style="font-size:6px;padding-left:32px;margin-top:24px">Anniversary wishes</p>
    <p class="copy" style="padding-left:33px">Lorem ipsum dolor sit amet, consectetur adipiscing elit. Sed ornare, metus non cursus volutpat, ligula odio faucibus turpis, non tincidunt nunc nunc quis elit.</p>
    <p class="hd" style="font-size:6px;padding-left:32px;margin-top:24px">visiting guests</p>
    <p class="copy" style="padding-left:33px">Lorem ipsum dolor sit amet, consectetur adipiscing elit. Sed ornare, metus non cursus volutpat, ligula odio faucibus turpis, non tincidunt nunc nunc quis elit. Lorem ipsum dolor sit amet, consectetur adipiscing elit. Sed ornare, metus non cursus volutpat, ligula odio faucibus turpis, non tincidunt nunc nunc quis elit.</p>
  </div>
  <div class="abs" style="left:0;top:429px;width:255px;height:25px;background:var(--white)"></div>
  <div class="abs brand" style="left:90px;top:436px;font-size:9px"><i style="width:9px;height:11px"></i>YOUR LOGO</div>
</section>

<!-- Portrait welcome, magenta -->
<section class="panel" style="left:674px;top:13px;width:254px;height:452px">
  <div class="photo" role="img" aria-label="City skyline tinted magenta" style="inset:0;background:linear-gradient(180deg,var(--magenta) 0%,#b7147f 55%,var(--plum) 100%)"></div>
  <svg class="abs" style="left:0;top:0" width="254" height="452" viewBox="0 0 254 452">
    <path d="M0 0H254C196 52 110 86 0 90Z" fill="#fff"/>
    <path d="M254 403C225 430 195 445 158 452H254Z" fill="#fff"/>
  </svg>
  <p class="abs" style="left:19px;top:17px;font-size:17px;font-weight:300;color:var(--ink);line-height:1">Welcome to</p>
  <p class="abs" style="left:19px;top:34px;font-size:17px;font-weight:700;color:var(--ink);line-height:1">Lorem Ipsum</p>
  <p class="abs clock" style="left:60px;top:103px;font-size:24px">11:24</p>
  <p class="abs date" style="left:63px;top:131px;font-size:6.5px">August 5 , 2018</p>
  <span class="divider" style="left:130px;top:100px;height:42px"></span>
  <div class="abs wx" style="left:141px;top:102px"><svg width="28" height="22"><use href="#icon-sun-cloud"/></svg><p style="font-size:5.5px;margin-top:4px">Currently Partly<br>Sunny 78°F</p></div>
  <div class="abs feed" style="left:52px;top:172px;width:160px;font-size:4.8px">
    <p class="hd" style="font-size:6.5px;border:0">News</p>
    <p class="copy">Lorem ipsum dolor sit amet, consectetur adipiscing elit. Sed ornare, metus non cursus volutpat, ligula odio faucibus turpis, non tincidunt nunc nunc quis elit.</p>
    <p class="hd" style="font-size:6.5px;border:0;margin-top:14px">Anniversary wishes</p>
    <p class="copy">Lorem ipsum dolor sit amet, consectetur adipiscing elit. Sed ornare, metus non cursus volutpat, ligula odio faucibus turpis, non tincidunt nunc nunc quis elit.</p>
    <p class="hd" style="font-size:6.5px;border:0;margin-top:14px">Visiting guests</p>
    <p class="copy">Lorem ipsum dolor sit amet, consectetur adipiscing elit. Sed ornare, metus non cursus volutpat, ligula odio faucibus turpis, non tincidunt nunc nunc quis elit.</p>
  </div>
  <p class="abs" style="left:0;width:254px;text-align:center;top:369px;font-size:6px;font-weight:700;line-height:1.7">Lorem ipsum dolor sit amet, consectetur adipiscing elit.<br>Consectetur adipiscing elit.</p>
  <div class="abs brand orange" style="left:195px;top:425px;font-size:6px;line-height:1"><i style="width:7px;height:7px"></i>LOREM<br>IPSUM</div>
</section>

<!-- Portrait welcome, dusk -->
<section class="panel" style="left:937px;top:13px;width:256px;height:455px">
  <div class="photo" role="img" aria-label="City lights at dusk with an orange horizon" style="inset:0;background:linear-gradient(180deg,var(--navy) 0%,#1f4c9e 28%,#5775ae 50%,#e08a52 62%,#56506f 70%,#1a2240 100%)"></div>
  <h1 class="abs welcome" style="left:0;width:256px;text-align:center;top:34px;font-size:40px">welcome</h1>
  <p class="abs lead" style="left:0;width:256px;text-align:center;top:82px;font-size:6.5px">Lorem ipsum dolor sit amet, consectetur adipiscing elit.</p>
  <p class="abs clock" style="left:28px;top:122px;font-size:36px">11:24</p>
  <p class="abs date" style="left:32px;top:163px;font-size:10px">August 5 , 2018</p>
  <span class="divider" style="left:132px;top:113px;height:75px"></span>
  <div class="abs wx" style="left:146px;top:118px"><svg width="42" height="34"><use href="#icon-sun-cloud"/></svg><p style="font-size:8.5px;margin-top:10px;margin-left:-5px">Currently Partly<br>Sunny 78°F</p></div>
  <div class="abs feed" style="left:12px;top:202px;width:230px;height:212px;border:.8px solid rgba(255,255,255,.6);background:rgba(13,39,99,.25);padding:12px 18px 0 0;font-size:4.5px">
    <p class="hd" style="font-size:6px;padding-left:24px">News</p>
    <p class="copy" style="padding-left:40px">Lorem ipsum dolor sit amet, consectetur adipiscing elit. Sed ornare, metus non cursus volutpat, ligula odio faucibus turpis, non tincidunt nunc nunc quis elit.</p>
    <p class="hd" style="font-size:6px;padding-left:40px;margin-top:20px">Anniversary wishes</p>
    <p class="copy" style="padding-left:40px">Lorem ipsum dolor sit amet, consectetur adipiscing elit. Sed ornare, metus non cursus volutpat, ligula odio faucibus turpis, non tincidunt nunc nunc quis elit.</p>
    <p class="hd" style="font-size:6px;padding-left:40px;margin-top:20px">visiting guests</p>
    <p class="copy" style="padding-left:40px">Lorem ipsum dolor sit amet, consectetur adipiscing elit. Sed ornare, metus non cursus volutpat, ligula odio faucibus turpis, non tincidunt nunc nunc quis elit. Lorem ipsum dolor sit amet, consectetur adipiscing elit. Sed ornare, metus non cursus volutpat, ligula odio faucibus turpis, non tincidunt nunc nunc quis elit.</p>
  </div>
  <div class="abs" style="left:0;top:433px;width:256px;height:22px;background:var(--blue-deep)"></div>
  <div class="abs brand light" style="left:97px;top:437px;font-size:12px"><i style="width:12px;height:12px"></i>LOGO</div>
</section>

<!-- Landscape welcome, blue (reduced) -->
<section class="panel" style="left:30px;top:785px;width:260px;height:146px;background:var(--white)">
  <div class="photo" role="img" aria-label="Blurred mountain valley landscape under a blue sky" style="left:0;top:0;width:145px;height:130px;background:linear-gradient(180deg,#3f6ed3 0%,#5b86d8 45%,#6b8fa0 70%,#6c6a4c 100%)"></div>
  <h2 class="abs welcome" style="left:15px;top:10px;font-size:24px">welcome</h2>
  <p class="abs lead" style="left:16px;top:36px;font-size:3.7px">Lorem ipsum dolor sit amet, consectetur adipiscing elit.</p>
  <p class="abs clock" style="left:16px;top:60px;font-size:20px">11:24</p>
  <p class="abs date" style="left:19px;top:84px;font-size:5.7px">August 5 , 2018</p>
  <span class="divider" style="left:75px;top:55px;height:42px"></span>
  <div class="abs wx" style="left:89px;top:58px"><svg width="24" height="19"><use href="#icon-sun-cloud"/></svg><p style="font-size:4.7px;margin-top:6px">Currently Partly<br>Sunny 78°F</p></div>
  <div class="abs brand" style="left:11px;top:134px;font-size:4.5px"><i style="width:5px;height:5px"></i>YOUR LOGO</div>
  <div class="abs feed" style="left:145px;top:0;width:115px;height:146px;background:var(--blue);padding:14px 8px 0 0;font-size:2.9px">
    <p class="hd" style="font-size:3.7px;padding-left:18px">News</p>
    <p class="copy" style="padding-left:18px">Lorem ipsum dolor sit amet, consectetur adipiscing elit. Sed ornare, metus non cursus volutpat, ligula odio faucibus turpis, non tincidunt nunc nunc quis elit.</p>
    <p class="hd" style="font-size:3.7px;padding-left:18px;margin-top:7px">Anniversary wishes</p>
    <p class="copy" style="padding-left:18px">Lorem ipsum dolor sit amet, consectetur adipiscing elit. Sed ornare, metus non cursus volutpat, ligula odio faucibus turpis, non tincidunt nunc nunc quis elit.</p>
    <p class="hd" style="font-size:3.7px;padding-left:18px;margin-top:7px">visiting guests</p>
    <p class="copy" style="padding-left:18px">Lorem ipsum dolor sit amet, consectetur adipiscing elit. Sed ornare, metus non cursus volutpat, ligula odio faucibus turpis, non tincidunt nunc nunc quis elit. Lorem ipsum dolor sit amet, consectetur adipiscing elit. Sed ornare, metus non cursus volutpat.</p>
  </div>
</section>

<!-- Meeting room, blue -->
<section class="panel" style="left:633px;top:522px;width:520px;height:293px;background:var(--charcoal)">
  <div class="photo" role="img" aria-label="Empty boardroom with a long table and chairs, tinted blue" style="left:0;top:0;width:326px;height:261px;background:linear-gradient(180deg,#4777d6 0%,#4a74cc 55%,#3f66bd 100%)"></div>
  <h1 class="abs welcome" style="left:27px;top:26px;font-size:35px">meeting room</h1>
  <p class="abs lead" style="left:27px;top:65px;font-size:7px">Lorem ipsum dolor sit amet, consectetur adipiscing elit.</p>
  <p class="abs clock" style="left:89px;top:124px;font-size:42px">11:24</p>
  <p class="abs date" style="left:93px;top:170px;font-size:12px">August 5 , 2018</p>
  <div class="abs" style="left:0;top:261px;width:326px;height:32px;background:var(--white)"></div>
  <div class="abs brand" style="left:27px;top:271px;font-size:10px"><i style="width:10px;height:13px"></i>YOUR LOGO</div>
  <p class="abs" style="left:354px;top:35px;font-size:9.5px;font-weight:700">NEXT</p>
  <p class="abs" style="left:354px;top:57px;font-size:9.5px;font-weight:700;color:#4f80e4">Lorem Ipsum dolor sit</p>
  <p class="abs" style="left:354px;top:70px;font-size:7px;font-weight:600">Lorem Ipsum dolor sit</p>
  <p class="abs" style="left:354px;top:85px;font-size:9.5px;font-weight:600">12:30 - 13:30</p>
  <span class="abs" style="left:354px;top:102px;width:143px;height:.8px;background:rgba(255,255,255,.5)"></span>
  <p class="abs" style="left:354px;top:117px;font-size:9.5px;font-weight:700;color:#4f80e4">Lorem Ipsum dolor sit</p>
  <p class="abs" style="left:354px;top:130px;font-size:7px;font-weight:600">Lorem Ipsum dolor sit</p>
  <p class="abs" style="left:354px;top:145px;font-size:9.5px;font-weight:600">13:30 - 14:10</p>
  <div class="btn" style="left:358px;top:218px;width:118px;height:21px;background:var(--blue);font-size:7px">BOOK NOW</div>
  <p class="abs" style="left:354px;top:263px;font-size:7px;font-weight:500">Lorem Ipsum dolor sit amet omen</p>
</section>

<!-- Meeting room, dark -->
<section class="panel" style="left:633px;top:830px;width:515px;height:290px">
  <div class="photo" role="img" aria-label="Dim conference room with a long table and office chairs" style="inset:0;background:linear-gradient(180deg,#2a2a2b 0%,#262626 50%,#1a1a1a 100%)"></div>
  <p class="abs" style="left:160px;top:34px;font-size:21px;font-weight:300">Meeting Room <span style="color:var(--orange)">B</span></p>
  <p class="abs clock" style="left:54px;top:94px;font-size:33px">11:24</p>
  <p class="abs date" style="left:57px;top:133px;font-size:10px">August 5 , 2018</p>
  <p class="abs" style="left:155px;top:98px;font-size:9px;color:var(--orange)">Lorem Ipsum dolor sit</p>
  <p class="abs" style="left:155px;top:110px;font-size:7px;font-weight:600">Lorem Ipsum dolor sit</p>
  <p class="abs" style="left:155px;top:125px;font-size:9px;font-weight:500">12:30 - 13:30</p>
  <p class="abs" style="left:155px;top:152px;font-size:7.5px;font-weight:700">NEXT</p>
  <p class="abs" style="left:155px;top:164px;font-size:9px;color:var(--orange)">Lorem Ipsum dolor sit</p>
  <p class="abs" style="left:155px;top:176px;font-size:7px;font-weight:600">Lorem Ipsum dolor sit</p>
  <p class="abs" style="left:155px;top:191px;font-size:9px;font-weight:500">12:30 - 13:30</p>
  <span class="abs" style="left:155px;top:209px;width:305px;height:.8px;background:rgba(255,255,255,.5)"></span>
  <svg class="abs" style="left:0;top:267px" width="104" height="23" viewBox="0 0 104 23"><path d="M0 0H104L96 23H0Z" fill="#fff"/></svg>
  <div class="abs brand orange" style="left:20px;top:274px;font-size:8px"><i style="width:8px;height:10px"></i>YOUR LOGO</div>
  <p class="abs" style="left:113px;top:262px;font-size:5px">7:00</p>
  <p class="abs" style="left:140px;top:262px;font-size:5px">8:00</p>
  <p class="abs" style="left:166px;top:262px;font-size:5px">9:00</p>
  <svg class="abs" style="left:114px;top:272px" width="233" height="10" viewBox="0 0 233 10">
    <rect width="233" height="10" fill="#3a3a3c"/>
    <rect x="29" width="45" height="10" fill="#58585b"/>
    <rect x="108" width="11" height="10" fill="#58585b"/>
    <rect x="185" width="23" height="10" fill="#58585b"/>
    <rect x="227" width="6" height="10" fill="#58585b"/>
  </svg>
  <p class="abs" style="left:358px;top:278px;font-size:7px;font-weight:600">AVAILABLE</p>
  <div class="btn" style="left:427px;top:271px;width:64px;height:16px;border-radius:8px;background:var(--orange);font-size:6px;font-weight:600">BOOK NOW</div>
</section>

</body>
</html>
```